website design + images

We need a very appealing website design, layout and images for a sales analytics and sales productivity services company based in San Ramon, California. We need a good design for the home page and a template for all other pages (total 2 designs), and images for all inner pages (center column/banner images, and right hand top corner small images). There are about 18 inner pages.
Updates

Our existing website is www.vorlaxen.com
Our corporate colours are the ones that are there on the website. The logo is also shown. We will be changing the tagline to "accelerating revenue" or equivalent of that.

Please use the document "website for vorlaxen - template v2.doc" that I just uploaded for any reference to the content, navigation and wireframes. A few more clarifications are provided mainly for the link "Solutions".

Devendra Kothuri

Hi,
We just uploaded ver 4 of the website template. There is more elaboration provided around the sublinks / sections for Solutions. Pls review and do get back if you need any clarifications.

Rgds
Devendra Kothuri

Hi all,
We have so far received a few good designs. The designs are more or less on the right track. I would like to urge all of you to use the content and navigation provided in the document attached to our brief "website for vorlaxen - template v4.doc".  Please DO NOT use the content in our existing website www.vorlaxen.com . That is very old. We mentioned it only for reference to colour theme and broad details.

We have totally 13 sections in Solutions pages. They may be designed as a tree of links - first level sublinks - second level sublinks or links - first level sublinks and the remaining as sections within the first level sublinks pages. The page design would remain the same for all inner pages except careers. But after finalizing the design for the inner page, we will need images for the different inner pages.

Rgds
Devendra Kothuri

Hi,
Thank you all for participation and very good designs. We are quite happy with what we have seen. We have now shortlisted about 4 vendors and sending invididual feedback to them for further improvement. We will be finalizing by Monday or Tuesday.  To the vendors who do not get feedback from us, thank you very much for participation. We may still do business in future for some of our other needs. 
The following are the process steps / expectations going forward, 
1. Feedback to the shortlisted designers and inviting improvements.
2. Review of the improved designs and further shortlist & feedback or direct finalization.
3. The design should be in 1024*768
2. Number of page designs = 2 (home page, inner page).
4. Home page design: instead of delivery model and customers, show one link "Why Us".
4. Solutions page design:  We will be needing an image in center column of solutions page that in a nutshell gives all the different types of solutions we provide. The entire set of solutions is in our attached document website for vorlaxen - template v4 and I am just uploading v5 with more description on sublinks.
5. After selection, we will be needing images for all the solution pages (total 12 pages under solutions + one solutions page), 1 image for Why Us?, 1 for Careers, and 3 for company (about us/ team, core values, ...) = total 18

Rgds
Devendra Kothuri

Target Market(s)

We are a sales analytics and sales productivity services company. We help B2B companies with: sales planning; sales operations and sales measurement. The characteristics of our customers are:
- B2B medium enterprises (USD 100M- USD 2B in revenue) in the US
- Primary target verticals are: high-tech, engineering and professional services firms
- Our primary target customers titles are VP of Sales or VP of marketing; we could be selling to the CEO at companies with revenues below $200M

Industry/Entity Type

Consulting

Requirements
Must have
• - Clean, uncluttered design
• - Easy navigation; minimum clicks
Nice to have
• We have already built a content management system and wireframes for this site. To the extent possible, it would be great to leverage the wireframe structure we built, provided you don’t have to compromise on the look and feel and navigation of the site. Below is what we currently have as banner sizes and resolutions are:
• Home page banner size: 950 * 250’
• All pages – center top - image size: 558 * 160
• All pages – right hand top image – 175*135’

```html
<!DOCTYPE html>
<html lang="en">
<head>
<meta charset="utf-8">
<title>Vorlaxen – Solutions</title>
<link rel="stylesheet" href="https://fonts.googleapis.com/css2?family=Arimo:wght@400;700&family=Roboto+Condensed:wght@700&family=Open+Sans:wght@400;700&display=swap">
<style>
:root{
  --blue:#0a6cb4;
  --blue-dark:#05549a;
  --link:#0a63b0;
  --green:#4a9a3a;
  --green-dark:#3b8a2e;
  --orange:#eea51b;
  --sky:#55abe6;
  --text:#222;
  --page-top:#ffffff;
  --page-bottom:#9b9b9b;
}
*{box-sizing:border-box;margin:0;padding:0}
html,body{width:1200px;height:798px;overflow:hidden}
body{
  position:relative;
  font-family:"Arimo",Arial,sans-serif;
  color:var(--text);
  background:linear-gradient(to bottom,var(--page-top) 0,#f7f7f7 150px,#e6e6e6 380px,var(--page-bottom) 798px);
}
a{text-decoration:none;color:inherit}

/* utility bar */
.utility-bar{position:absolute;left:0;top:0;width:1200px;height:42px;background:linear-gradient(to bottom,#1a7cc4,var(--blue-dark))}
.utility-bar a{position:absolute;top:0;height:42px;display:flex;align-items:center;gap:6px;color:#fff;font-size:13.5px;letter-spacing:-.3px;white-space:nowrap}
.utility-bar .icon{width:20px;height:20px;flex:none}
.sign-in{left:54px;width:162px;height:50px!important;padding-left:8px;background:linear-gradient(to bottom,#5fb34a,var(--green-dark));border-radius:0 0 4px 4px;box-shadow:0 1px 2px rgba(0,0,0,.3)}
.contact{left:226px}
.sitemap{left:355px}

/* header */
.brand{position:absolute;left:62px;top:104px;font-size:30px;font-weight:400;color:var(--blue);line-height:1}

.main-nav{position:absolute;left:744px;top:116px;display:flex;align-items:center;font-size:14.5px;font-weight:700;color:var(--link)}
.main-nav a{padding:4px 8px}
.main-nav .current{background:linear-gradient(to bottom,#5cad47,var(--green-dark));color:#fff;border-radius:13px;border:1px solid #2f7a24;padding:3px 12px;margin:0 2px}
.main-nav .sep{color:var(--green);font-weight:400}

/* content panel */
.content-panel{position:absolute;left:48px;top:175px;width:1089px;height:585px;background:#fff;border-radius:0 0 12px 12px}

/* sidebar */
.sidebar{position:absolute;left:57px;top:185px;width:214px}
.side-head{height:38px;display:flex;align-items:center;gap:8px;padding-left:9px;font-family:"Roboto Condensed",sans-serif;font-size:14.5px;color:var(--green);background:linear-gradient(to bottom,#fff,#dcdcdc);border:1px solid #d4d4d4;border-radius:4px 4px 0 0;white-space:nowrap}
.side-head .toggle{width:15px;height:15px;border-radius:2px;background:var(--green);display:flex;align-items:center;justify-content:center;flex:none}
.side-list{list-style:none;padding:12px 8px 10px 8px;background:linear-gradient(to bottom,#f1f1f1,#fff 30px)}
.side-list li{font-size:12px;height:25px;display:flex;align-items:center;gap:6px;padding-left:3px;border-bottom:1px dotted #aaa;color:#222}
.side-list li.active{font-weight:700;font-size:12.5px}
.side-list li::before{content:"›";font-size:11px;color:#333}
.side-head.collapsed{margin-top:7px;border-radius:4px}
.sidebar-shade{position:absolute;left:270px;top:185px;width:2px;height:510px;background:linear-gradient(to bottom,#ddd,rgba(221,221,221,0))}

/* banner */
.banner{position:absolute;left:284px;top:185px;width:626px;height:181px;background:linear-gradient(100deg,#0a5ea6 0%,#1f86d0 45%,#6fb8ea 70%,#1b6fb6 100%)}
.banner-photo{position:absolute;inset:0}
.banner-copy{position:absolute;left:13px;top:95px;color:#fff;font-family:"Open Sans",sans-serif}
.banner-copy h2{font-size:24px;font-weight:700;letter-spacing:-.5px;line-height:1.1}
.banner-copy p{font-size:15.5px;font-weight:700;line-height:19px;margin-top:2px;letter-spacing:-.2px}

/* solutions */
.section-title{position:absolute;left:290px;top:375px;font-family:"Roboto Condensed",sans-serif;font-size:26px;color:var(--green)}
.solution-card{position:absolute;top:412px;width:196px;height:332px;border:1px solid #e2e2e2;border-radius:10px;background:#fff;padding:17px 13px 0 13px}
.card-planning{left:290px}
.card-productivity{left:502px}
.card-measurement{left:711px}
.card-photo{height:78px}
.card-label{height:66px;padding:8px 12px;color:#fff}
.card-label h3{font-family:"Roboto Condensed",sans-serif;font-size:14px;line-height:15px}
.card-label p{font-size:12px;margin-top:8px}
.card-planning .card-label{background:var(--green)}
.card-productivity .card-label{background:var(--orange)}
.card-measurement .card-label{background:var(--sky)}
.card-planning .card-photo{background:linear-gradient(135deg,#d9d9d9,#8d8d8d 60%,#555)}
.card-productivity .card-photo{background:linear-gradient(135deg,#3a6aa0,#d6e4f2 55%,#b8863a)}
.card-measurement .card-photo{background:linear-gradient(135deg,#e3e8ec,#d76a45 60%,#c94a2a)}
.card-intro{font-size:13.5px;line-height:16px;margin-top:10px;color:#111}
.card-links{list-style:none;margin-top:11px}
.card-links li{font-size:13.5px;line-height:16.2px;color:var(--link);padding-left:12px;position:relative}
.card-links li::before{content:"›";position:absolute;left:0;top:0;font-size:11px;color:var(--green)}
.card-intro.tight + .card-links{margin-top:3px}

/* right column */
.aside{position:absolute;left:926px;top:185px;width:196px}
.aside-photo{height:150px;background:linear-gradient(140deg,#d8d5cf,#9fa9b3 45%,#3e4a58 80%,#7a6a58)}
.aside-band{height:31px;background:var(--green);color:#fff;font-family:"Roboto Condensed",sans-serif;font-size:14px;display:flex;align-items:center;padding-left:8px}
.aside-text{padding:15px 10px 0 12px;font-size:13px;line-height:19px;text-align:justify;color:#111}
.aside-text p+p{margin-top:19px}
.aside-shade{position:absolute;left:925px;top:185px;width:1px;height:530px;background:linear-gradient(to bottom,#ddd,rgba(221,221,221,0))}

/* footer */
.site-footer{position:absolute;left:59px;top:771px;width:1064px;display:flex;justify-content:space-between;color:#fff;font-size:13.5px}
</style>
</head>
<body>

<nav class="utility-bar">
  <a class="sign-in" href="#">
    <svg class="icon" viewBox="0 0 20 20"><circle cx="10" cy="10" r="10" fill="#fff"/><path d="M7 5h7v10H7" fill="none" stroke="#3b8a2e" stroke-width="1.6"/><path d="M4 10h7M9 7.5l2.5 2.5L9 12.5" fill="none" stroke="#3b8a2e" stroke-width="1.6"/></svg>
    SIGN IN / REGISTER
  </a>
  <a class="contact" href="#">
    <svg class="icon" viewBox="0 0 20 20"><circle cx="10" cy="10" r="10" fill="#fff"/><rect x="8" y="4.5" width="4" height="3.5" fill="none" stroke="#3b8a2e" stroke-width="1.3"/><rect x="4" y="11.5" width="4" height="3.5" fill="none" stroke="#3b8a2e" stroke-width="1.3"/><rect x="12" y="11.5" width="4" height="3.5" fill="none" stroke="#3b8a2e" stroke-width="1.3"/><path d="M10 8v2M6 11.5V10h8v1.5" fill="none" stroke="#3b8a2e" stroke-width="1.3"/></svg>
    CONTACT&nbsp; US
  </a>
  <a class="sitemap" href="#">
    <svg class="icon" viewBox="0 0 20 20"><circle cx="10" cy="10" r="10" fill="#fff"/><rect x="4.5" y="6" width="11" height="8" fill="none" stroke="#3b8a2e" stroke-width="1.3"/><path d="M4.5 6l5.5 4.5L15.5 6" fill="none" stroke="#3b8a2e" stroke-width="1.3"/></svg>
    SITEMAP
  </a>
</nav>

<header>
  <a class="brand" href="#">Vorlaxen</a>
  <nav class="main-nav">
    <a href="#">Home</a>
    <a class="current" href="#">Solutions</a>
    <a href="#">Why Us</a><span class="sep">|</span>
    <a href="#">Company</a><span class="sep">|</span>
    <a href="#">Careers</a>
  </nav>
</header>

<div class="content-panel"></div>

<aside class="sidebar">
  <div class="side-head"><span class="toggle"><svg width="9" height="6" viewBox="0 0 9 6"><path d="M0 0h9L4.5 6z" fill="#fff"/></svg></span>Sales Planning Analytics</div>
  <ul class="side-list">
    <li>Customer Targeting</li>
    <li>Territory Planning</li>
    <li class="active">Campaign Planning</li>
  </ul>
  <div class="side-head collapsed"><span class="toggle"><svg width="6" height="9" viewBox="0 0 6 9"><path d="M0 0v9l6-4.5z" fill="#fff"/></svg></span>Sales Productivity Centers</div>
  <div class="side-head collapsed"><span class="toggle"><svg width="6" height="9" viewBox="0 0 6 9"><path d="M0 0v9l6-4.5z" fill="#fff"/></svg></span>Sales Measurement Analytics</div>
</aside>
<div class="sidebar-shade"></div>

<main>
  <section class="banner">
    <div class="banner-photo" role="img" aria-label="Silhouettes of business people shaking hands on a glowing blue network floor"></div>
    <div class="banner-copy">
      <h2>Do more with less.</h2>
      <p>No upfront software, hardware,<br>people or training costs for you. Pay as you go.</p>
    </div>
  </section>

  <h1 class="section-title">Solutions</h1>

  <article class="solution-card card-planning">
    <div class="card-photo" role="img" aria-label="Hands reviewing charts and papers at a desk"></div>
    <div class="card-label"><h3>Sales Planning<br>Analytics</h3><p>Sell to the right customers</p></div>
    <p class="card-intro">We help target the right customers, allocate resources effectively and increase return on sales &amp; marketing $.</p>
    <ul class="card-links"><li>Customer Targeting</li><li>Territory Planning</li><li>Campaign Planning</li></ul>
  </article>

  <article class="solution-card card-productivity">
    <div class="card-photo" role="img" aria-label="Sales representatives with headsets in an office"></div>
    <div class="card-label"><h3>Sales Productivity<br>Centers</h3><p>Spend more time selling</p></div>
    <p class="card-intro tight">This is all about saving time for sales reps and improv-ing their productivity.</p>
    <ul class="card-links"><li>Quoting center</li><li>Proposal center</li><li>CRM center</li><li>Partner center</li><li>Reference center</li><li>Deal center</li></ul>
  </article>

  <article class="solution-card card-measurement">
    <div class="card-photo" role="img" aria-label="Rising red bar chart graphic"></div>
    <div class="card-label"><h3>Sales Measurement<br>Analytics</h3><p>Sell more efficiently.</p></div>
    <p class="card-intro tight">This is all about improving sales efficiency by providing actionable insights.</p>
    <ul class="card-links"><li>Business Reporting</li><li>Metrics &amp; Benchmarking</li><li>Pipeline health check</li><li>Sales rep scorecards</li><li>What-if analyses</li><li>Data services.</li></ul>
  </article>
</main>

<div class="aside-shade"></div>
<aside class="aside">
  <div class="aside-photo" role="img" aria-label="Colleagues reviewing documents at a meeting table"></div>
  <div class="aside-band">Sales Operations Support</div>
  <div class="aside-text">
    <p>Vestibulum lectus arcu, iaculis non iaculis ultrices, ultricies sit amet nisi. Nullam dictum nunc et metus dapibus scelerisque. Etiam quis sapien in purus consequat ornare.</p>
    <p>Praesent vitae ipsum lorem. Nullam ac orci mi, sed pellen-tesque dolor. Nullam dictum nunc et metus dapibus scelerisque. Etiam quis sapien in purus consequat ornare. Praesent vitae ipsum lorem. Nullam ac orci mi, sed pellen-tesque dolor.</p>
  </div>
</aside>

<footer class="site-footer">
  <span>Contact Us | Sitemap &nbsp;| &nbsp;Disclaimer</span>
  <span>© 2010. Vorlaxen, Inc. All Rights Reserved</span>
</footer>

</body>
</html>
```